Looking for a modern website banner design

Bramblecrest Coaching Partners looking for the development of the main banner of the website. The project description and photos are included in the upload files.

```html
<!DOCTYPE html>
<html lang="en">
<head>
<meta charset="utf-8">
<title>Bramblecrest Coaching Partners – Website Banner Options</title>
<link href="https://fonts.googleapis.com/css2?family=Roboto:wght@400;500;700&display=swap" rel="stylesheet">
<style>
  :root {
    --page-bg: #ffffff;
    --ink-dark: #1c1d21;
    --slate: #2f3b4c;
    --brand-blue: #0f77c0;
    --steel: #4a6282;
    --text-light: #ffffff;
    --text-accent: #d3d6db;
  }
  * { margin: 0; padding: 0; box-sizing: border-box; }
  html, body {
    width: 1200px;
    height: 800px;
    overflow: hidden;
    background: var(--page-bg);
    font-family: "Roboto", Arial, sans-serif;
  }
  .canvas { position: relative; width: 1200px; height: 800px; }
  .banner {
    position: absolute;
    left: 218px;
    width: 772px;
    height: 362px;
    overflow: hidden;
  }
  .banner--crowd { top: 31px; }
  .banner--ice { top: 421px; }
  .banner-art { position: absolute; inset: 0; width: 772px; height: 362px; }
  .testimonial-quote {
    position: absolute;
    left: 50px;
    color: var(--text-light);
    font-size: 17.6px;
    line-height: 21.7px;
    font-weight: 400;
    letter-spacing: 0.05px;
    white-space: nowrap;
  }
  .banner--crowd .testimonial-quote { top: 84px; }
  .banner--ice .testimonial-quote { top: 87px; }
  .testimonial-quote strong { color: var(--text-accent); font-weight: 700; }
  .testimonial-quote .plain { color: var(--text-light); font-weight: 400; }
  .attribution {
    position: absolute;
    color: var(--text-light);
    white-space: nowrap;
  }
  .banner--crowd .attribution { left: 252px; top: 243px; }
  .banner--ice .attribution { left: 246px; top: 256px; }
  .attribution-name {
    font-size: 14px;
    font-weight: 500;
    letter-spacing: 0.1px;
  }
  .attribution-name .dash { display: inline-block; width: 12px; }
  .attribution-role {
    padding-left: 12px;
    font-size: 9.8px;
    line-height: 12.2px;
    font-weight: 500;
  }
</style>
</head>
<body>
<main class="canvas">

  <section class="banner banner--crowd">
    <svg class="banner-art" viewBox="0 0 772 362" aria-hidden="false">
      <defs>
        <linearGradient id="band-a" x1="0" y1="0" x2="1" y2="0">
          <stop offset="0" stop-color="var(--ink-dark)"/>
          <stop offset="0.17" stop-color="var(--slate)"/>
          <stop offset="0.30" stop-color="var(--brand-blue)"/>
          <stop offset="0.42" stop-color="var(--steel)"/>
          <stop offset="0.62" stop-color="var(--ink-dark)"/>
          <stop offset="1" stop-color="var(--ink-dark)"/>
        </linearGradient>
        <linearGradient id="photo-a" x1="0" y1="0" x2="1" y2="1">
          <stop offset="0" stop-color="#7a2a33"/>
          <stop offset="0.45" stop-color="#2a3446"/>
          <stop offset="0.75" stop-color="#b3262f"/>
          <stop offset="1" stop-color="#3a3434"/>
        </linearGradient>
      </defs>
      <rect width="772" height="362" fill="url(#band-a)"/>
      <circle cx="649" cy="203" r="241" fill="url(#photo-a)" role="img"
              aria-label="Photo: smiling pro hockey player in team jersey high-fiving young fans leaning over the tunnel rail"/>
      <circle cx="649" cy="203" r="241" fill="none" stroke="var(--brand-blue)" stroke-width="3.5"/>
    </svg>
    <p class="testimonial-quote">“Bramblecrest has provided support that has<br>allowed me to develop as a person and<br>an athlete.&nbsp; The P.A.T.H.S.™ process<br>allowed me to stay focused on<br><strong>attainable goals each season</strong> <span class="plain">and</span><br><strong>progress from Junior to College</strong> <span class="plain">and</span><br>now <strong>Professional Hockey</strong>.”</p>
    <div class="attribution">
      <p class="attribution-name"><span class="dash">-</span>MARCUS DELORME</p>
      <p class="attribution-role">Riverton Gales<br>Atlantic Pro Hockey Circuit</p>
    </div>
  </section>

  <section class="banner banner--ice">
    <svg class="banner-art" viewBox="0 0 772 362" aria-hidden="false">
      <defs>
        <linearGradient id="band-b" x1="0" y1="0" x2="1" y2="0">
          <stop offset="0" stop-color="var(--ink-dark)"/>
          <stop offset="0.17" stop-color="var(--slate)"/>
          <stop offset="0.30" stop-color="var(--brand-blue)"/>
          <stop offset="0.42" stop-color="var(--steel)"/>
          <stop offset="0.62" stop-color="var(--ink-dark)"/>
          <stop offset="1" stop-color="var(--ink-dark)"/>
        </linearGradient>
        <linearGradient id="photo-b" x1="0" y1="0" x2="0" y2="1">
          <stop offset="0" stop-color="#3b3236"/>
          <stop offset="0.5" stop-color="#5a4a52"/>
          <stop offset="0.72" stop-color="#c9cfd8"/>
          <stop offset="1" stop-color="#eef1f5"/>
        </linearGradient>
      </defs>
      <rect width="772" height="362" fill="url(#band-b)"/>
      <circle cx="649" cy="203" r="241" fill="url(#photo-b)" role="img"
              aria-label="Photo: hockey player raising his stick in celebration on the ice in front of a cheering crowd, opponent skating past"/>
      <circle cx="649" cy="203" r="241" fill="none" stroke="var(--brand-blue)" stroke-width="3.5"/>
    </svg>
    <p class="testimonial-quote">“Bramblecrest has provided support that has<br>allowed me to develop as a person and<br>an athlete.&nbsp; The P.A.T.H.S.™ process<br>allowed me to stay focused on<br><strong>attainable goals each season</strong> <span class="plain">and</span><br><strong>progress from Junior to College</strong> <span class="plain">and</span><br>now <strong>Professional Hockey</strong>.”</p>
    <div class="attribution">
      <p class="attribution-name"><span class="dash">-</span>MARCUS DELORME</p>
      <p class="attribution-role">Riverton Gales<br>Atlantic Pro Hockey Circuit</p>
    </div>
  </section>

</main>
</body>
</html>
```